The Perfect Business Card for Tavoranth

I am looking for a business card which beautifully incorporates my logo, reflects my business and looks special, elegant and clean.

```html
<!DOCTYPE html>
<html lang="en">
<head>
<meta charset="utf-8">
<title>Tavoranth Business Card</title>
<link rel="stylesheet" href="https://fonts.googleapis.com/css2?family=Open+Sans:wght@300;400;700&display=swap">
<style>
  :root {
    --leaf: #87a84b;
    --moss: #556b30;
    --olive: #6e8c34;
    --navy: #2e3192;
    --paper: #ffffff;
    --edge: #b9b9b9;
  }
  * { margin: 0; padding: 0; box-sizing: border-box; }
  html, body { width: 1200px; height: 1000px; overflow: hidden; background: var(--paper); }
  body { position: relative; font-family: "Open Sans", Arial, sans-serif; }

  .band { position: absolute; left: 0; width: 1200px; height: 20px; display: flex; }
  .band span { flex: 1; }
  .band--top { top: 0; }
  .band--bottom { bottom: 0; }
  .band--top .band__left, .band--bottom .band__right { background: var(--leaf); }
  .band--top .band__right, .band--bottom .band__left { background: var(--moss); }

  .card { position: absolute; background: var(--leaf); border: 1px solid var(--edge); overflow: hidden; }
  .card--front { left: 80px; top: 85px; width: 708px; height: 393px; }
  .card--back { left: 426px; top: 503px; width: 707px; height: 392px; }
  .card__curve { position: absolute; inset: 0; width: 100%; height: 100%; }

  .brand { position: absolute; display: flex; align-items: center; gap: 10px; }
  .brand__dot { width: 22px; height: 22px; border-radius: 50%; background: var(--olive); }
  .brand__name { font-family: "Open Sans", Arial, sans-serif; font-weight: 400; font-size: 38px; color: var(--olive); letter-spacing: 0.5px; }
  .card--front .brand { left: 48px; top: 270px; }
  .card--back .brand { left: 400px; top: 268px; }

  .identity, .contact { position: absolute; left: 458px; border-left: 2px solid var(--navy); padding-left: 19px; color: var(--navy); }
  .identity { top: 198px; }
  .identity__name { font-weight: 700; font-size: 24px; line-height: 28px; }
  .identity__role { font-weight: 300; font-size: 15px; line-height: 18px; }
  .contact { top: 259px; font-weight: 300; font-size: 16px; line-height: 25.5px; }
</style>
</head>
<body>
  <div class="band band--top"><span class="band__left"></span><span class="band__right"></span></div>

  <section class="card card--front">
    <svg class="card__curve" viewBox="0 0 708 393" preserveAspectRatio="none" aria-hidden="true">
      <path d="M0,250 C70,200 190,180 280,212 C350,240 383,310 383,393 L0,393 Z" fill="#ffffff"/>
    </svg>
    <div class="brand">
      <span class="brand__dot"></span>
      <span class="brand__name">Tavoranth</span>
    </div>
    <div class="identity">
      <p class="identity__name">Tavoranth</p>
      <p class="identity__role">General Manager</p>
    </div>
    <div class="contact">
      <p>0123456789</p>
      <p>hello@tavoranth.com</p>
      <p>www.tavoranth.com</p>
    </div>
  </section>

  <section class="card card--back">
    <svg class="card__curve" viewBox="0 0 707 392" preserveAspectRatio="none" aria-hidden="true">
      <path d="M324,392 C324,290 420,200 555,195 C625,193 680,222 707,249 L707,392 Z" fill="#ffffff"/>
    </svg>
    <div class="brand">
      <span class="brand__dot"></span>
      <span class="brand__name">Tavoranth</span>
    </div>
  </section>

  <div class="band band--bottom"><span class="band__left"></span><span class="band__right"></span></div>
</body>
</html>
```